Brisbane IT support business needs our first business card

Hello we are a Brisbane based Information Technology company providing support and services to small and medium sized businesses. We provide a range of services and solutions.

The business name is Wattlebrook Network Computing Services, or WNCS for short.

I am looking for a business card that looks professional (don't we all want that), but most importantly, it most utilize the colours in the logo attached.

Reason: Launched late, extending so people have enough time to actually submit something.

Target Market(s)

Other business owners seeking our IT services, and also home users.

Industry/Entity Type

Business

Requirements
Must have
• Please only use the blue/orange colours in logo attached

```html
<!DOCTYPE html>
<html lang="en">
<head>
<meta charset="utf-8">
<title>WNCS Business Card</title>
<link rel="stylesheet" href="https://fonts.googleapis.com/css2?family=Mulish:wght@700;800&family=Questrial&display=swap">
<style>
  :root {
    --navy: #0f4a66;
    --orange: #ec7d24;
    --paper: #ffffff;
    --backdrop: #b8774f;
  }
  html, body {
    margin: 0;
    width: 1200px;
    height: 900px;
    overflow: hidden;
    background: var(--backdrop);
  }
  .stage { position: relative; width: 1200px; height: 900px; }
  .card {
    position: absolute;
    background: var(--paper);
    overflow: hidden;
    box-shadow: 0 3px 8px rgba(0,0,0,0.35);
    font-family: "Mulish", sans-serif;
  }
  .card-front { left: 352px; top: 150px; width: 496px; height: 284px; }
  .card-back { left: 352px; top: 466px; width: 494px; height: 272px; }

  .brand { position: absolute; display: flex; align-items: center; }
  .brand-mark { border-radius: 50%; background: var(--navy); flex: none; }
  .brand-text { color: var(--orange); font-weight: 800; line-height: 1; }
  .brand-name { display: block; letter-spacing: 0.5px; }
  .brand-full { display: block; letter-spacing: 0.2px; }

  .card-front .brand { left: 18px; top: 20px; }
  .card-front .brand-mark { width: 56px; height: 56px; margin-right: 14px; }
  .card-front .brand-name { font-size: 26px; }
  .card-front .brand-full { font-size: 5.6px; margin-top: 3px; }

  .contact {
    position: absolute;
    right: 14px;
    top: 70px;
    text-align: right;
    color: var(--navy);
    font-weight: 700;
  }
  .contact-name { font-size: 26px; font-weight: 800; margin: 0 0 6px; line-height: 1.1; }
  .contact-line { font-size: 18.5px; margin: 0 0 7px; line-height: 1.1; }

  .band-navy-front { position: absolute; left: 0; top: 234px; width: 100%; height: 30px; background: var(--navy); }
  .band-orange-front { position: absolute; left: 0; top: 264px; width: 100%; height: 20px; background: var(--orange); }
  .web {
    position: absolute; left: 0; top: 234px; width: 100%; height: 30px;
    line-height: 30px; text-align: center;
    font-family: "Questrial", sans-serif;
    color: var(--orange); font-size: 20px; letter-spacing: 5px;
  }

  .band-orange-back { position: absolute; left: 0; top: 0; width: 100%; height: 72px; background: var(--orange); }
  .band-navy-back { position: absolute; left: 0; bottom: 0; width: 100%; height: 40px; background: var(--navy); }
  .card-back .brand { left: 114px; top: 91px; }
  .card-back .brand-mark { width: 88px; height: 88px; margin-right: 28px; }
  .card-back .brand-name { font-size: 42px; }
  .card-back .brand-full { font-size: 9.4px; margin-top: 5px; }
</style>
</head>
<body>
<main class="stage">
  <section class="card card-front">
    <div class="brand">
      <span class="brand-mark"></span>
      <span class="brand-text">
        <span class="brand-name">WNCS</span>
        <span class="brand-full">WATTLEBROOK NETWORK<br>COMPUTING SERVICES</span>
      </span>
    </div>
    <div class="contact">
      <p class="contact-name">Daniel Hartley</p>
      <p class="contact-line">Managing Director</p>
      <p class="contact-line">Telephone: 555.013.2846</p>
      <p class="contact-line">Email: info@wncs.net</p>
    </div>
    <div class="band-navy-front"></div>
    <div class="band-orange-front"></div>
    <div class="web">www.wncs.net</div>
  </section>

  <section class="card card-back">
    <div class="band-orange-back"></div>
    <div class="brand">
      <span class="brand-mark"></span>
      <span class="brand-text">
        <span class="brand-name">WNCS</span>
        <span class="brand-full">WATTLEBROOK NETWORK<br>COMPUTING SERVICES</span>
      </span>
    </div>
    <div class="band-navy-back"></div>
  </section>
</main>
</body>
</html>
```